Stationery Design Project - Technica-Prime

Business Cards
Size: 90mm x 55mm

Letterhead
Size: A4 - 210mm x 297mm

With Compliments Slip
Size: DL - 210mm x 99mm

Notepad
Size: 250mm x 140mm

Presentation Folder
Size: A4

Technica-Prime
*Perth *Brisbane *Seoul *Hongkong

website: www.technicaprime-example.com.au (Currently live, but being replaced with new one)

Engineering and Technical recruitment company for the Mining, Oil & Gas, Construction & Engineering Sectors

Industry/Entity Type

Business

```html
<!DOCTYPE html>
<html lang="en">
<head>
<meta charset="utf-8">
<title>Technica-Prime — With Compliments Slip</title>
<link rel="stylesheet" href="https://fonts.googleapis.com/css2?family=Open+Sans:wght@300;400;600&display=swap">
<style>
  :root {
    --backdrop: #e9eaec;
    --paper: #ffffff;
    --navy: #16277a;
    --blue: #1f63c9;
    --sky: #3fa3e6;
    --ink: #2b2d33;
    --grey: #7c8088;
  }
  * { margin: 0; padding: 0; box-sizing: border-box; }
  html, body {
    width: 1200px; height: 885px; overflow: hidden;
    background: var(--backdrop);
    font-family: "Open Sans", Arial, sans-serif;
  }
  .slip {
    position: absolute; left: 100px; top: 207px;
    width: 1000px; height: 471px;
    background: var(--paper);
    box-shadow: 0 2px 10px rgba(0,0,0,0.08);
    overflow: hidden;
  }
  .brand {
    position: absolute; left: 42px; top: 34px;
    display: flex; align-items: center; gap: 12px;
  }
  .brand-dot {
    width: 30px; height: 30px; border-radius: 50%;
    background: var(--blue);
  }
  .brand-name {
    font-weight: 300; font-size: 30px; letter-spacing: 1px;
    color: var(--grey);
  }
  .contact {
    position: absolute; left: 42px; top: 200px;
    color: var(--ink); font-size: 11px; line-height: 15px;
  }
  .contact-name { font-size: 14px; margin-bottom: 4px; }
  .contact-name strong { color: var(--navy); font-weight: 600; }
  .contact-address { margin-bottom: 4px; }
  .contact-lines { display: grid; grid-template-columns: auto auto; column-gap: 14px; row-gap: 2px; }
  .contact-item { display: flex; align-items: center; gap: 5px; }
  .contact-item svg { width: 11px; height: 11px; flex: none; }
  .greeting {
    position: absolute; right: 60px; top: 168px;
    font-size: 32px; font-weight: 400; color: var(--navy);
  }
  .rule {
    position: absolute; left: 0; bottom: 28px;
    width: 780px; height: 5px;
    background: linear-gradient(90deg, var(--navy) 0%, var(--blue) 40%, var(--sky) 75%, var(--navy) 100%);
  }
</style>
</head>
<body>
  <main class="slip">
    <div class="brand">
      <span class="brand-dot"></span>
      <span class="brand-name">technicaprime</span>
    </div>

    <address class="contact" style="font-style:normal">
      <p class="contact-name"><strong>Harlow</strong> | President</p>
      <p class="contact-address">Level 4, 18 Carden St, WEST RIDGE<br>NSW 2199, Australia</p>
      <div class="contact-lines">
        <span class="contact-item">
          <svg viewBox="0 0 12 12"><circle cx="6" cy="6" r="6" fill="#16277a"/><path d="M3.6 3.2c.4-.4.9-.3 1.1.1l.5.9c.2.3 0 .6-.2.8l-.3.3c.3.8.9 1.4 1.7 1.7l.3-.3c.2-.2.5-.4.8-.2l.9.5c.4.2.5.7.1 1.1-.6.6-1.5.7-2.5.1C4.9 7.6 4.3 7 3.7 6c-.6-1-.6-2 0-2.8z" fill="#fff"/></svg>
          600 555 0142
        </span>
        <span class="contact-item">
          <svg viewBox="0 0 12 12"><circle cx="6" cy="6" r="6" fill="#16277a"/><text x="6" y="8.6" font-size="8" text-anchor="middle" fill="#fff" font-family="Arial, sans-serif">@</text></svg>
          harlow@technicaprime-example.com.au
        </span>
        <span class="contact-item">
          <svg viewBox="0 0 12 12"><circle cx="6" cy="6" r="6" fill="#16277a"/><rect x="3" y="5" width="6" height="3.5" rx="0.5" fill="#fff"/><rect x="4" y="3" width="4" height="2" fill="#fff"/></svg>
          600 555 0187
        </span>
        <span class="contact-item">
          <svg viewBox="0 0 12 12"><circle cx="6" cy="6" r="6" fill="#16277a"/><circle cx="6" cy="6" r="3.2" fill="none" stroke="#fff" stroke-width="0.8"/><path d="M2.8 6h6.4M6 2.8c-1.4 1.8-1.4 4.6 0 6.4M6 2.8c1.4 1.8 1.4 4.6 0 6.4" fill="none" stroke="#fff" stroke-width="0.7"/></svg>
          www.technicaprime-example.com.au
        </span>
      </div>
    </address>

    <h1 class="greeting">With Best Compliments</h1>

    <div class="rule"></div>
  </main>
</body>
</html>
```